Web site design for BrixaForm Software (www.brixaformsoftware.example)

Need the design as well as the html for the website. The brief is given in the attached file.
If possible, would like to use pencil sketches instead of images to give a unique look to the site.
Target Market(s)
small Software product companies
Industry/Entity Type
Software
Coding
Coded - Design and coding required
Number of Pages Required
5+ page

```html
<!DOCTYPE html>
<html lang="en">
<head>
<meta charset="utf-8">
<title>BrixaForm Software</title>
<link href="https://fonts.googleapis.com/css2?family=Marcellus&family=Open+Sans:ital,wght@0,400;0,600;0,700;1,400&display=swap" rel="stylesheet">
<style>
:root{
  --white:#ffffff;
  --ink:#333333;
  --text:#666666;
  --nav:#555555;
  --band:#5a5a5a;
  --services:#6b6b6b;
  --blog-card:#333333;
  --footer:#3b3b3b;
  --hero-a:#1f2a36;
  --hero-b:#2f3b48;
  --line:#9a9a9a;
  --soft:#d8d8d8;
}
*{margin:0;padding:0;box-sizing:border-box}
html,body{width:1200px;height:3509px;overflow:hidden}
body{font-family:"Open Sans",Arial,sans-serif;color:var(--text);background:var(--white);position:relative}
.serif{font-family:"Marcellus",Georgia,serif;font-weight:400}
.abs{position:absolute}

/* header */
.site-header{position:absolute;left:0;top:0;width:1200px;height:103px;background:var(--white)}
.brand{left:76px;top:34px;font-size:34px;letter-spacing:3px;color:var(--ink);font-weight:700}
.brand span{font-weight:400}
.contact-chip{top:32px;display:flex;align-items:center;gap:14px;font-size:17px;color:var(--text)}
.chip-icon{width:40px;height:40px;border-radius:50%;background:#e2e2e2;display:flex;align-items:center;justify-content:center}
.main-nav{position:absolute;left:0;top:103px;width:1200px;height:54px;background:var(--nav);display:flex;justify-content:center;gap:28px;align-items:center}
.main-nav a{color:var(--white);text-decoration:none;font-size:17px;padding:12px 0}
.main-nav a.active{border-bottom:2px solid var(--white)}

/* hero */
.hero{position:absolute;left:0;top:157px;width:1200px;height:521px;background:linear-gradient(160deg,var(--hero-b),var(--hero-a));color:var(--white);text-align:center}
.hero h1{position:absolute;left:0;width:100%;top:150px;font-size:56px;font-family:"Marcellus",Georgia,serif;font-weight:400}
.hero .quote{position:absolute;left:250px;width:700px;top:232px;font-style:italic;font-size:19px;line-height:33px}
.hero .author{position:absolute;left:0;width:100%;top:305px;font-size:19px}
.hero-arrow{position:absolute;top:233px;width:40px;height:42px;background:rgba(255,255,255,.35);display:flex;align-items:center;justify-content:center}
.hero-dots{position:absolute;top:470px;left:560px;display:flex;gap:6px}
.hero-dots i{width:16px;height:16px;border-radius:50%;border:2px solid var(--white);display:block}
.hero-dots i.on{background:var(--white)}

/* welcome */
.welcome{position:absolute;top:678px;left:0;width:1200px;height:351px;text-align:center}
.section-title{font-family:"Marcellus",Georgia,serif;font-weight:400;font-size:40px;color:var(--ink)}
.welcome h2{margin-top:38px;font-size:34px}
.welcome p{width:800px;margin:10px auto 0;font-size:15px;line-height:24px}
.btn-dark{display:inline-block;background:var(--nav);color:var(--white);font-size:19px;padding:6px 18px;margin-top:16px}

/* clients */
.clients{position:absolute;top:1029px;left:0;width:1200px;height:206px;background:var(--band);text-align:center;color:var(--white)}
.clients h2{color:var(--white);margin-top:34px}
.clients hr{width:1010px;margin:8px auto 0;border:0;border-top:1px solid var(--line)}
.client-row{position:absolute;top:112px;left:125px;width:950px;display:flex;justify-content:space-between;align-items:center}
.client-name{font-family:"Open Sans",Arial,sans-serif;font-weight:600;font-size:38px;color:#e6e6e6}
.client-arrow{position:absolute;top:118px;font-size:34px;color:var(--white)}

/* background */
.background{position:absolute;top:1235px;left:0;width:1200px;height:468px}
.background h2{position:absolute;left:77px;top:85px;font-size:42px}
.background .copy{position:absolute;left:77px;top:143px;width:470px;font-size:15px;line-height:24px}
.background .copy p+p{margin-top:4px}
.btn-outline{position:absolute;left:77px;top:352px;border:1px solid var(--ink);color:var(--ink);font-size:19px;padding:6px 14px}
.sketch{position:absolute;left:603px;top:15px;width:597px;height:453px;background:linear-gradient(135deg,#fafafa,#e9e9e9)}

/* services */
.services{position:absolute;top:1703px;left:0;width:1200px;height:772px;background:var(--services);color:var(--white)}
.services h2{position:absolute;top:36px;width:100%;text-align:center;color:var(--white);font-size:40px}
.svc{position:absolute;font-family:"Marcellus",Georgia,serif;font-size:23px;line-height:26px}
.svc small{display:block;font-family:"Open Sans",Arial,sans-serif;font-size:15px;letter-spacing:.5px}
.svc.left{text-align:right}
.svc.center{text-align:center;width:240px;left:479px}

/* testimonials */
.testimonials{position:absolute;top:2475px;left:0;width:1200px;height:273px}
.testimonials h2{position:absolute;top:40px;width:100%;text-align:center;font-size:40px}
.quote-badge{position:absolute;left:124px;top:2612px}
.avatar{position:absolute;left:146px;top:2593px;width:92px;height:92px;border-radius:50%;background:linear-gradient(135deg,#c9b6a8,#8b7b70);border:3px solid var(--white);box-shadow:0 0 0 1px #ccc}
.testimonial-text{position:absolute;left:283px;top:2602px;width:780px;font-style:italic;font-size:15px;line-height:26px}
.client-sign{position:absolute;left:890px;top:2672px;font-weight:700;font-size:15px;color:var(--ink)}
.t-arrow{position:absolute;top:2618px;font-size:36px;color:var(--ink)}

/* blog */
.blog{position:absolute;top:2748px;left:0;width:1200px;height:375px;background:var(--band)}
.blog h2{position:absolute;top:36px;width:100%;text-align:center;color:var(--white);font-size:40px}
.post{position:absolute;top:96px;width:440px;height:228px;background:var(--blog-card);color:var(--white)}
.post-img{position:absolute;left:0;top:0;width:180px;height:228px;background:linear-gradient(160deg,#9aa3ad,#4d5560)}
.post-img.warm{background:linear-gradient(160deg,#e4ddd3,#a6958a)}
.date{position:absolute;width:66px;height:88px;background:var(--white);color:var(--ink);text-align:center;font-weight:700}
.date b{display:block;font-size:24px;margin-top:10px}
.date span{font-size:14px}
.post-body{position:absolute;left:200px;top:18px;width:225px}
.post-body h3{font-size:17px;line-height:24px;font-weight:700}
.post-body p{font-size:14px;line-height:23px;margin-top:12px}

/* footer */
.site-footer{position:absolute;top:3123px;left:0;width:1200px;height:386px;background:var(--footer);color:var(--white)}
.site-footer h4{font-family:"Marcellus",Georgia,serif;font-weight:400;font-size:21px}
.sitemap{position:absolute;left:80px;top:38px}
.sitemap ul{list-style:none;position:absolute;top:40px;width:200px}
.sitemap li{font-size:15px;line-height:27px;padding-left:24px;position:relative}
.sitemap li::before{content:"";position:absolute;left:0;top:7px;width:13px;height:13px;border-radius:50%;background:var(--white)}
.contact-info{position:absolute;left:442px;top:38px;width:320px}
.contact-info .item{position:relative;padding-left:34px;font-size:15px;line-height:21px;margin-top:14px}
.contact-info svg{position:absolute;left:0;top:2px}
.newsletter{position:absolute;left:802px;top:38px;width:330px}
.newsletter p{font-size:15px;line-height:24px;margin-top:12px}
.newsletter .field{margin-top:12px;width:322px;height:42px;background:var(--white);color:#888;font-size:14px;padding:11px 10px}
.newsletter .subscribe{margin-top:10px;width:143px;height:40px;background:#888;color:var(--white);font-size:17px;text-align:center;line-height:40px}
.footer-rule{position:absolute;left:80px;top:332px;width:1040px;border-top:1px solid #777}
.copyright{position:absolute;top:350px;width:100%;text-align:center;font-size:15px}
</style>
</head>
<body>

<header class="site-header">
  <div class="abs brand">BRIXA<span>FORM</span></div>
  <div class="abs contact-chip" style="left:646px">
    <span class="chip-icon"><svg width="20" height="14" viewBox="0 0 20 14"><rect x="1" y="1" width="18" height="12" fill="none" stroke="#777" stroke-width="1.6"/><path d="M1 1l9 7 9-7" fill="none" stroke="#777" stroke-width="1.6"/></svg></span>
    info@brixaform.example
  </div>
  <div class="abs contact-chip" style="left:916px">
    <span class="chip-icon"><svg width="18" height="18" viewBox="0 0 24 24"><path d="M6 2l4 5-2 3c1 2 3 4 6 6l3-2 5 4-3 4C10 21 3 14 2 5z" fill="#777"/></svg></span>
    +353 (0)86 5550142
  </div>
</header>

<nav class="main-nav">
  <a class="active">Home</a><a>About us</a><a>Experties</a><a>Angile</a><a>Case Studies</a><a>Career</a><a>Accolades</a><a>Stories</a><a>Partners</a><a>Giving Back</a><a>Blog</a><a>Contact Us</a>
</nav>

<section class="hero" role="img" aria-label="Dark sketched desk scene with drafting tools, a keyboard, a tablet and hands at work">
  <h1>infecting engineering with design</h1>
  <p class="quote">“Perfection is achieved not when there is nothing more to add, but when there is nothing left to take away.”</p>
  <p class="author">-Aurelien Vasseur</p>
  <span class="hero-arrow" style="left:36px"><svg width="12" height="18"><path d="M10 2L3 9l7 7" fill="none" stroke="#fff" stroke-width="2"/></svg></span>
  <span class="hero-arrow" style="left:1122px"><svg width="12" height="18"><path d="M2 2l7 7-7 7" fill="none" stroke="#fff" stroke-width="2"/></svg></span>
  <div class="hero-dots"><i class="on"></i><i></i><i></i><i></i></div>
</section>

<section class="welcome">
  <h2 class="section-title">Welcome Visitors!</h2>
  <p>Design pervades nature. Whether it is the unique symmetry of a snowflake, or the fibonnacci number of a sunflower or nautilus shell, or self replicating fractals, design is everywhere.</p>
  <p>In todays world, Good Design is associated more with tangible products, and User interfaces. But good design has always been part of software engineering. Good design is what enables massive software edifices to remain stable. Good design is UI and UX of course, but it also the process of deciding “what” is required, “how” it is to be built, “who” will build it, and how will its goodness perpetuate itself.</p>
  <span class="btn-dark">KNOW MORE</span>
</section>

<section class="clients">
  <h2 class="section-title">Our Clients</h2>
  <hr>
  <span class="client-arrow" style="left:64px">‹</span>
  <div class="client-row">
    <span class="client-name">Lumora</span>
    <span class="client-name">grovex</span>
    <span class="client-name">KESTREL</span>
    <span class="client-name">TANVIO</span>
    <span class="client-name">Pixora</span>
  </div>
  <span class="client-arrow" style="left:1118px">›</span>
</section>

<section class="background">
  <h2 class="section-title">Background and Expertise</h2>
  <div class="copy">
    <p>We are primarily server side programmers with expertise in large scale projects – be it Software development tools, Distributed software frameworks, Telecom and mediation software or Business intelligence.</p>
    <p>Over the years, we have been the trusted offshore product development partner for many startups and mid sized software product companies, and have built software products from scratch.</p>
  </div>
  <span class="btn-outline">KNOW MORE</span>
  <div class="sketch" role="img" aria-label="Pencil sketch of hands typing on a laptop beside notes, a sticky pad and a chart"></div>
</section>

<section class="services">
  <h2 class="section-title">Our Services</h2>
  <svg class="abs" style="left:0;top:0" width="1200" height="772" viewBox="0 0 1200 772">
    <circle cx="599" cy="418" r="258" fill="none" stroke="#bdbdbd" stroke-width="2"/>
    <rect x="510" y="128" width="182" height="356" rx="24" fill="none" stroke="#cfcfcf" stroke-width="3"/>
    <rect x="522" y="172" width="158" height="270" fill="#7a7a7a" stroke="#cfcfcf" stroke-width="1.5"/>
    <rect x="585" y="150" width="32" height="5" rx="2" fill="#cfcfcf"/>
    <rect x="586" y="450" width="30" height="22" rx="5" fill="none" stroke="#cfcfcf" stroke-width="2"/>
    <g fill="#6b6b6b" stroke="#dcdcdc" stroke-width="2">
      <circle cx="416" cy="180" r="33"/><circle cx="370" cy="304" r="33"/><circle cx="370" cy="430" r="33"/><circle cx="451" cy="547" r="33"/>
      <circle cx="599" cy="585" r="33"/>
      <circle cx="783" cy="180" r="33"/><circle cx="828" cy="304" r="33"/><circle cx="828" cy="430" r="33"/><circle cx="747" cy="547" r="33"/>
    </g>
    <g fill="none" stroke="#dcdcdc" stroke-width="1.6">
      <rect x="406" y="166" width="20" height="28"/><rect x="360" y="294" width="20" height="20"/><rect x="360" y="418" width="18" height="24"/>
      <rect x="440" y="537" width="22" height="20"/><rect x="586" y="575" width="26" height="20"/>
      <rect x="773" y="170" width="20" height="20"/><rect x="816" y="296" width="24" height="16"/><rect x="818" y="418" width="18" height="24"/><path d="M739 557l8-18 8 18"/>
    </g>
  </svg>
  <div class="svc left" style="left:156px;top:162px;width:200px">POC<small>READ MORE</small></div>
  <div class="svc left" style="left:106px;top:286px;width:200px">Build Product<small>READ MORE</small></div>
  <div class="svc left" style="left:106px;top:413px;width:200px">Maintain Product<small>READ MORE</small></div>
  <div class="svc left" style="left:184px;top:530px;width:200px">ODC Setup<small>READ MORE</small></div>
  <div class="svc" style="left:845px;top:162px">POC<small>READ MORE</small></div>
  <div class="svc" style="left:891px;top:286px">Build Product<small>READ MORE</small></div>
  <div class="svc" style="left:891px;top:413px">Maintain Product<small>READ MORE</small></div>
  <div class="svc" style="left:812px;top:530px">ODC Setup<small>READ MORE</small></div>
  <div class="svc center" style="top:645px">Architectural<br>Interventions<small>READ MORE</small></div>
</section>

<section class="testimonials">
  <h2 class="section-title">Testimonials</h2>
</section>
<span class="t-arrow" style="left:74px">‹</span>
<svg class="quote-badge" width="70" height="70" viewBox="0 0 70 70"><circle cx="35" cy="35" r="33" fill="#fff" stroke="#ccc" stroke-width="2"/><text x="20" y="50" font-family="Georgia,serif" font-size="44" fill="#333">“</text></svg>
<div class="avatar" role="img" aria-label="Round client portrait"></div>
<p class="testimonial-text">" Lorem Ipsum is simply dummy text of the printing and typesetting industry. Lorem Ipsum has been the industry's standard dummy text ever since the 1500s, when an unknown printer took a galley of type and scrambled it to make a type specimen book. "</p>
<span class="client-sign">— Client Name</span>
<span class="t-arrow" style="left:1105px">›</span>

<section class="blog">
  <h2 class="section-title">Latest Blog</h2>
  <article class="post" style="left:112px">
    <div class="post-img" role="img" aria-label="Photo of a computer keyboard and monitor"></div>
    <div class="date" style="left:114px;top:20px"><b>29</b><span>APR</span></div>
    <div class="post-body"><h3>Lorem Ipsum is simply dummy text.</h3><p>Lorem Ipsum is simply dummy text of the printing and typesetting industry. Lorem Ipsum has been the industry's standard.</p></div>
  </article>
  <article class="post" style="left:648px">
    <div class="post-img warm" role="img" aria-label="Photo of a smiling woman holding a tablet"></div>
    <div class="date" style="left:114px;top:120px"><b>29</b><span>APR</span></div>
    <div class="post-body"><h3>Lorem Ipsum is simply dummy text.</h3><p>Lorem Ipsum is simply dummy text of the printing and typesetting industry. Lorem Ipsum has been the industry's standard.</p></div>
  </article>
</section>

<footer class="site-footer">
  <div class="sitemap">
    <h4>Sitemap</h4>
    <ul style="left:0"><li>Home</li><li>About us</li><li>Experties</li><li>Angile</li><li>Case Studies</li><li>Career</li></ul>
    <ul style="left:182px"><li>Accolades</li><li>Stories</li><li>Partners</li><li>Giving Back</li><li>Blog</li><li>Contact Us</li></ul>
  </div>
  <div class="contact-info">
    <h4>Contact Info</h4>
    <div class="item"><svg width="20" height="24" viewBox="0 0 20 24"><path d="M10 1a8 8 0 0 1 8 8c0 6-8 14-8 14S2 15 2 9a8 8 0 0 1 8-8z" fill="none" stroke="#fff" stroke-width="1.6"/><circle cx="10" cy="9" r="3" fill="none" stroke="#fff" stroke-width="1.6"/></svg>Office 204, 7 Orchard Lane, Riverside Link Road, Nashik India - 422005</div>
    <div class="item"><svg width="20" height="24" viewBox="0 0 20 24"><path d="M10 1a8 8 0 0 1 8 8c0 6-8 14-8 14S2 15 2 9a8 8 0 0 1 8-8z" fill="none" stroke="#fff" stroke-width="1.6"/><circle cx="10" cy="9" r="3" fill="none" stroke="#fff" stroke-width="1.6"/></svg>BrixaForm Software (C/O CommonDesk) Office B3 Glenmore West Ballykeel Co.Carlow, Dublin Ireland</div>
    <div class="item"><svg width="18" height="18" viewBox="0 0 24 24"><path d="M6 2l4 5-2 3c1 2 3 4 6 6l3-2 5 4-3 4C10 21 3 14 2 5z" fill="none" stroke="#fff" stroke-width="1.8"/></svg>+353 (0)86 5550142</div>
  </div>
  <div class="newsletter">
    <h4>Newsletter</h4>
    <p>Would you like to receive exclusive access to articles, white papers and our regular monthly newsletter?</p>
    <div class="field">Enter Email Id</div>
    <div class="subscribe">SUBSCRIBE</div>
  </div>
  <div class="footer-rule"></div>
  <p class="copyright">©BRIXAFORM- 2017. All Rights Reserved.</p>
</footer>

</body>
</html>
```